Full Service Outdoor Property Management Company

We are looking for a new and fresh business card design. My company has been in business for 26 years. Winter: We are a large snow and ice management company that does work for commercial, industrial and municipal clients. We have been named "Top 100 Snow Companies in the U.S." for numerous years. Summer: We provide complete landscape maintenance and landscape design and construction for both residential and commercial clients. We must incorporate our logo into card design as well as (in no particular order):
Employees name
Office: (313) 847-2036
Cell: (xxx) xxx-xxxx
thornvale.com
1837 Wrenfield, Inkster MI 48139
(Something about 26 + years in business as well as "Top 100 snow contractors as stated above)
Target Market(s)
Winter: Commercial, Industrial, Municipal
Summer: Residential and Commercial
Industry/Entity Type
Construction
Contact Information for Business Card
This is a little challenging as we are using one card for essentially two companies that target different customers from summer to winter. Perhaps the back side could be split in two or something to highlight the different services?? I'm open to any ideas!! Looking forward to seeing what you come up with!
Requirements
Must have
- Logo
- (in no particular order)
- Employees name
- Office: (313) 847-2036
- Cell: (xxx) xxx-xxxx
- thornvale.com
- 1837 Wrenfield, Inkster MI 48139
Nice to have
- Something about 26 + years in business
- "Top 100 Snow Contractors in the U.S."
Should not have
- Cheesy pictures of lawn mowers and snow plows

```html
<!DOCTYPE html>
<html lang="en">
<head>
<meta charset="utf-8">
<title>Thornvale Incorporated — Business Card</title>
<link rel="stylesheet" href="https://fonts.googleapis.com/css2?family=Open+Sans:wght@400;700&family=Tinos:wght@700&display=swap">
<style>
  :root {
    --page-bg: #e9ebea;
    --card-white: #ffffff;
    --brand-green: #0f7a3a;
    --brand-green-light: #2a9a5e;
    --brand-blue: #1f8ae6;
    --ink: #222222;
    --text-on-green: #ffffff;
  }
  * { margin: 0; padding: 0; box-sizing: border-box; }
  html, body {
    width: 1200px; height: 900px; overflow: hidden;
    background: var(--page-bg);
    font-family: "Open Sans", Arial, sans-serif;
  }
  .canvas { position: relative; width: 1200px; height: 900px; }
  .card {
    position: absolute; left: 320px;
    width: 560px; height: 320px;
    background: var(--card-white);
    box-shadow: 0 6px 18px rgba(0,0,0,.18);
    overflow: hidden;
  }
  .card--front { top: 110px; }
  .card--back { top: 470px; }
  .card__shapes { position: absolute; inset: 0; width: 100%; height: 100%; }

  .years-badge {
    position: absolute; top: 14px; right: 18px;
    color: var(--text-on-green); font-weight: 700; font-size: 13px;
    letter-spacing: .5px; transform: rotate(20deg);
  }
  .front-identity {
    position: absolute; top: 96px; left: 0; right: 0;
    text-align: center;
  }
  .company-name {
    color: var(--brand-green); font-weight: 700;
    font-family: "Open Sans", Arial, sans-serif;
  }
  .front-identity .company-name { font-size: 34px; }
  .tagline {
    margin-top: 18px; color: var(--brand-green);
    font-size: 13px; line-height: 1.2;
  }
  .website { margin-top: 10px; color: var(--ink); font-size: 13px; letter-spacing: .3px; }

  .back-identity { position: absolute; top: 40px; left: 28px; width: 230px; }
  .back-identity .company-name { font-size: 22px; line-height: 1.15; }

  .contact {
    position: absolute; top: 78px; left: 336px;
    color: var(--text-on-green);
  }
  .contact__name, .contact__title {
    font-family: "Tinos", "Times New Roman", serif; font-weight: 700;
    font-size: 19px; letter-spacing: .4px; line-height: 1.15;
    white-space: nowrap;
  }
  .contact__title { margin-left: 10px; font-size: 17px; }
  .contact__lines { margin-top: 30px; margin-left: 30px; font-size: 14px; line-height: 1.3; white-space: nowrap; }
  .contact__address { margin-top: 14px; margin-left: 22px; font-size: 14px; line-height: 1.3; white-space: nowrap; }
</style>
</head>
<body>
<main class="canvas">

  <section class="card card--front" aria-label="Business card front">
    <svg class="card__shapes" viewBox="0 0 560 320" preserveAspectRatio="none" aria-hidden="true">
      <polygon points="0,200 300,320 0,320" fill="var(--brand-green)"/>
      <polygon points="400,0 560,0 560,75" fill="var(--brand-blue)"/>
    </svg>
    <div class="years-badge">26+ YEARS</div>
    <div class="front-identity">
      <div class="company-name">Thornvale Incorporated</div>
      <p class="tagline">Top 100 Snow Contractors<br>in the U.S</p>
      <p class="website">www.thornvale.com</p>
    </div>
  </section>

  <section class="card card--back" aria-label="Business card back">
    <svg class="card__shapes" viewBox="0 0 560 320" preserveAspectRatio="none" aria-hidden="true">
      <defs>
        <linearGradient id="greenPanel" x1="0" y1="0" x2="1" y2="0">
          <stop offset="0" stop-color="var(--brand-green)"/>
          <stop offset="1" stop-color="var(--brand-green-light)"/>
        </linearGradient>
      </defs>
      <polygon points="365,0 395,0 75,320 40,320" fill="var(--brand-blue)"/>
      <polygon points="395,0 560,0 560,320 75,320" fill="url(#greenPanel)"/>
    </svg>
    <div class="back-identity">
      <div class="company-name">Thornvale<br>Incorporated</div>
    </div>
    <div class="contact">
      <p class="contact__name">EMPLOYEES NAME</p>
      <p class="contact__title">TITLE</p>
      <p class="contact__lines">Office: (313) 847-2036<br>Cell: (xxx) xxx-xxxx</p>
      <p class="contact__address">1837 Wrenfield,<br>Inkster MI 48139</p>
    </div>
  </section>

</main>
</body>
</html>
```